Stationary Set Rebrand for Brenvik

We are a Canadian Distribution and Service Company that was established in 1969. Over the past 5 decades we have expanded our business and have warehouses across Canada. We specialize in adhesive tapes, adhesives, films, safety, warehouse, shipping, janitorial and packaging supplies.

We have updated our logo design and would like a new corporate branding identity that includes a new fresh Stationary Set (Business Cards, Letterhead, Letterhead MS Word, Envelope, Presentation Folders, Email Signatures, Notepad Covers, etc.)

Target Market(s)

Industrial Business Sector

Font styles to use
Sans Serif

Colors
0054AA
0677BA
7BADD7
CADEEF
E8F1F8
0094D4
00A9DD
6FCCEA
C7EBF8
E9F6FB
00AB8E
00BBA5
67D7C9
C6EFE9
E9F9F6
EB3D1F
EC4F4E
F09395
F8D3D4
FCEDEE

Requirements
Should not have
• Colors not too light, darker colours preferred

```html
<!DOCTYPE html>
<html lang="en">
<head>
<meta charset="utf-8">
<title>Brenvik Stationery Set</title>
<link href="https://fonts.googleapis.com/css2?family=Montserrat:wght@400;500;600;700;800&display=swap" rel="stylesheet">
<style>
:root{
  --bg:#dcdcdd;
  --paper:#f4f4f4;
  --paper-shade:#ebebeb;
  --ink:#231f20;
  --text:#3a3a3a;
  --muted:#6b6b6b;
  --red:#d71f26;
  --white:#ffffff;
}
*{box-sizing:border-box;margin:0;padding:0}
html,body{width:1200px;height:739px;overflow:hidden}
body{background:var(--bg);font-family:"Montserrat",sans-serif;color:var(--text);position:relative}
.piece{position:absolute;background:var(--paper);box-shadow:0 2px 6px rgba(0,0,0,.18);overflow:hidden}
.piece.dark{background:var(--ink)}

/* logo lockup */
.logo{position:absolute;line-height:1}
.logo-row{display:flex;align-items:center;gap:.1em}
.logo-name{font-weight:800;color:var(--ink);letter-spacing:-.02em}
.logo-mark{width:.26em;height:.26em;background:var(--red);display:inline-block}
.logo-tag{font-weight:600;color:var(--ink);font-size:.19em;margin-top:.2em;white-space:nowrap}
.logo.light .logo-name,.logo.light .logo-tag{color:var(--white)}

/* footer band */
.band{position:absolute;left:0;right:0;bottom:0;background:var(--ink);color:var(--white);display:flex;align-items:center;white-space:nowrap}
.band::after{content:"";position:absolute;right:0;top:0;bottom:0;width:14%;background:var(--red)}
.band span{position:relative;z-index:1}

.contacts{position:absolute;list-style:none}
.contacts li{display:flex;align-items:center;gap:.4em;white-space:nowrap}
.contacts svg{width:.9em;height:.9em;fill:var(--red);flex:none}
.vrule{position:absolute;width:1px;background:var(--red)}

/* business cards */
.card-front{left:46px;top:82px;width:154px;height:90px}
.card-front .logo{left:37px;top:8px;font-size:17px}
.card-front .person{position:absolute;left:10px;top:48px;text-align:right;width:66px;white-space:nowrap}
.card-front .person b{display:block;font-size:5px;color:var(--ink)}
.card-front .person i{font-style:normal;font-size:4px;color:var(--red)}
.card-front .vrule{left:80px;top:43px;height:22px}
.card-front .contacts{left:83px;top:42px;font-size:4px;line-height:6px;color:var(--ink)}
.card-front .band{height:7px;font-size:3.8px;padding-left:29px}
.card-back{left:211px;top:82px;width:154px;height:90px;border-radius:6px}
.card-back .logo{left:23px;top:28px;font-size:24px}

/* email signature */
.signature{left:394px;top:78px;width:282px;height:99px}
.signature .logo{left:38px;top:27px;font-size:22px}
.signature .vrule{left:147px;top:14px;height:55px}
.signature .who{position:absolute;left:157px;top:14px;white-space:nowrap}
.signature .who b{display:block;font-size:8px;color:var(--red);font-weight:800}
.signature .who i{display:block;font-style:normal;font-size:6.2px;color:var(--ink);margin-top:3px}
.signature .contacts{left:157px;top:40px;font-size:6.2px;line-height:10px;color:var(--ink)}
.signature .band{height:11px;bottom:6px;font-size:6px;justify-content:center}

/* letterhead */
.letterhead{left:39px;top:192px;width:330px;height:469px}
.letterhead .logo{left:28px;top:27px;font-size:19px}
.letterhead .vrule{left:219px;top:26px;height:27px}
.letterhead .contacts{left:223px;top:25px;font-size:6.4px;line-height:10.2px;color:var(--ink)}
.recipient{position:absolute;left:28px;top:108px;white-space:nowrap}
.recipient b{display:block;font-size:6.4px;font-weight:600;color:var(--ink)}
.recipient i{font-style:normal;font-size:4.6px;font-weight:600;color:var(--ink)}
.date{position:absolute;right:29px;top:116px;font-size:5px;color:var(--muted);white-space:nowrap}
.letter-body{position:absolute;left:28px;right:28px;top:139px;font-size:4.7px;line-height:8px;color:var(--muted);text-align:justify}
.letter-body p+p{margin-top:8px}
.sign-area{position:absolute;left:28px;top:322px;width:74px;height:18px;background:linear-gradient(90deg,#d8d8d8,#ececec);border-radius:2px}
.signer{position:absolute;left:28px;top:351px}
.signer b{display:block;font-size:6.4px;font-weight:600;color:var(--ink)}
.signer i{font-style:normal;font-size:4.8px;color:var(--muted)}
.letterhead .band{height:15px;bottom:10px;font-size:5.8px;justify-content:center}

/* compliments slip */
.compliments{left:387px;top:192px;width:294px;height:151px}
.compliments .logo{left:15px;top:15px;font-size:19px}
.compliments .address{position:absolute;left:15px;top:75px;font-size:5.4px;line-height:8.3px;color:var(--ink)}
.compliments .contacts{position:static;font-size:5.4px;line-height:8.3px}
.compliments .band{height:14px;bottom:11px;font-size:5.6px;font-weight:700;padding-left:15px}

/* envelopes */
.envelope-back{left:387px;top:357px;width:294px;height:145px}
.flap{position:absolute;left:0;top:0;width:294px;height:48px}
.envelope-back .logo{left:114px;top:15px;font-size:15px}
.envelope-front{left:387px;top:512px;width:294px;height:149px}
.envelope-front .logo{left:17px;top:14px;font-size:16.5px}
.window{position:absolute;left:16px;top:79px;width:110px;height:34px;background:var(--paper-shade);border-radius:4px}
.envelope-front .band{height:13px;bottom:12px;font-size:5.2px;padding-left:16px}

/* folder, outside */
.folder-cover{left:708px;top:48px;width:226px;height:292px}
.folder-cover .logo{left:22px;top:196px;font-size:23px}
.cover-lines{position:absolute;left:22px;top:236px;font-size:4.6px;line-height:8px;color:var(--white);white-space:nowrap}
.cover-lines .rule{height:1px;background:var(--red);margin:2px 0 3px;width:180px}
.folder-back{left:942px;top:48px;width:226px;height:292px}
.folder-back .logo{left:40px;top:28px;font-size:24px}
.folder-back .band{height:14px;bottom:14px;font-size:5px;justify-content:center}

/* folder, inside */
.folder-open{left:708px;top:357px;width:446px;height:304px;background:none;box-shadow:none;overflow:visible}
.panel{position:absolute;top:0;height:304px;width:223px;background:var(--paper);box-shadow:0 2px 6px rgba(0,0,0,.18);overflow:hidden}
.panel.left{left:0}
.panel.right{left:223px;background:var(--paper-shade)}
.pocket{position:absolute;bottom:0;height:80px;width:223px}
.panel.left .logo{left:57px;top:248px;font-size:21px}
.mini-letter{position:absolute;left:18px;top:18px;width:187px;height:210px;background:var(--paper);box-shadow:0 1px 3px rgba(0,0,0,.15)}
.mini-letter .logo{left:16px;top:14px;font-size:10.5px}
.mini-letter .contacts{left:128px;top:14px;font-size:3.4px;line-height:5.6px;color:var(--ink)}
.mini-letter .recipient{left:16px;top:60px}
.mini-letter .recipient b{font-size:3.6px}
.mini-letter .recipient i{font-size:2.6px}
.mini-letter .date{right:16px;top:64px;font-size:2.6px}
.mini-letter .letter-body{left:16px;right:16px;top:78px;font-size:2.7px;line-height:4.6px}
.mini-letter .sign-area{left:16px;top:184px;width:40px;height:9px}
.mini-letter .signer{left:16px;top:198px}
.mini-letter .signer b{font-size:3.4px}
.mini-card{position:absolute;left:86px;top:240px;width:76px;height:44px;background:var(--paper);box-shadow:0 1px 3px rgba(0,0,0,.3);overflow:hidden}
.mini-card .logo{left:19px;top:4px;font-size:8.5px}
.mini-card .person{position:absolute;left:4px;top:22px;width:34px;text-align:right;font-size:2.5px;font-weight:700;color:var(--ink);white-space:nowrap}
.mini-card .person i{display:block;font-style:normal;font-weight:400;color:var(--red);font-size:2.1px}
.mini-card .contacts{left:41px;top:21px;font-size:2.1px;line-height:3.3px;color:var(--ink)}
.mini-card .band{height:4px;font-size:1.9px;padding-left:12px}
</style>
</head>
<body>

<svg width="0" height="0" style="position:absolute" aria-hidden="true">
  <defs>
    <symbol id="i-phone" viewBox="0 0 16 16"><path d="M3 2h3l1.5 3.5-2 1.3a9 9 0 0 0 3.7 3.7l1.3-2L14 10v3a1 1 0 0 1-1 1A11 11 0 0 1 2 3a1 1 0 0 1 1-1z"/></symbol>
    <symbol id="i-mail" viewBox="0 0 16 16"><path d="M1 3h14v10H1zM2 4.2v.6l6 4 6-4v-.6z"/></symbol>
    <symbol id="i-web" viewBox="0 0 16 16"><path d="M8 1a7 7 0 1 0 0 14A7 7 0 0 0 8 1zm0 1.5c.9 0 2 1.7 2.3 4.5H5.7C6 4.2 7.1 2.5 8 2.5zM2.6 7h1.6a12 12 0 0 1 0 2H2.6a5.6 5.6 0 0 1 0-2zm9.2 0h1.6a5.6 5.6 0 0 1 0 2h-1.6a12 12 0 0 0 0-2zM5.7 9h4.6c-.3 2.8-1.4 4.5-2.3 4.5S6 11.8 5.7 9z"/></symbol>
  </defs>
</svg>

<!-- business card, front -->
<section class="piece card-front">
  <div class="logo"><div class="logo-row"><span class="logo-name">Brenvik</span><span class="logo-mark"></span></div><div class="logo-tag">Tape and Packaging Specialists</div></div>
  <div class="person"><b>MARCUS DELANEY</b><i>Founder &amp; CEO</i></div>
  <div class="vrule"></div>
  <ul class="contacts">
    <li><svg><use href="#i-phone"/></svg>548-555-0142</li>
    <li><svg><use href="#i-phone"/></svg>548-555-0142</li>
    <li><svg><use href="#i-mail"/></svg>info@brenviksales.com</li>
    <li><svg><use href="#i-web"/></svg>www.brenviksales.com</li>
  </ul>
  <div class="band"><span>22-180 Birchwood Ave, Guelph, ON N1H 4K7</span></div>
</section>

<!-- business card, back -->
<section class="piece dark card-back">
  <div class="logo light"><div class="logo-row"><span class="logo-name">Brenvik</span><span class="logo-mark"></span></div><div class="logo-tag">Tape and Packaging Specialists</div></div>
</section>

<!-- email signature -->
<section class="piece signature">
  <div class="logo"><div class="logo-row"><span class="logo-name">Brenvik</span><span class="logo-mark"></span></div><div class="logo-tag">Tape and Packaging Specialists</div></div>
  <div class="vrule"></div>
  <div class="who"><b>MARCUS DELANEY</b><i>Controls Engineer</i></div>
  <ul class="contacts">
    <li><svg><use href="#i-phone"/></svg>548-555-0142</li>
    <li><svg><use href="#i-mail"/></svg>info@brenviksales.com</li>
    <li><svg><use href="#i-web"/></svg>www.brenviksales.com</li>
  </ul>
  <div class="band"><span>22-180 Birchwood Ave, Guelph, ON N1H 4K7</span></div>
</section>

<!-- letterhead -->
<section class="piece letterhead">
  <div class="logo"><div class="logo-row"><span class="logo-name">Brenvik</span><span class="logo-mark"></span></div><div class="logo-tag">Tape and Packaging Specialists</div></div>
  <div class="vrule"></div>
  <ul class="contacts">
    <li><svg><use href="#i-phone"/></svg>548-555-0142</li>
    <li><svg><use href="#i-mail"/></svg>info@brenviksales.com</li>
    <li><svg><use href="#i-web"/></svg>www.brenviksales.com</li>
  </ul>
  <div class="recipient"><b>Dear. Mrs Clara Anne Whitfield</b><i>Chief Director</i></div>
  <div class="date">Date: 16-October-2025</div>
  <div class="letter-body">
    <p>Lorem ipsum dolor sit amet, consectetur adipiscing elit, sed do eiusmod tempor incididunt ut labore et dolore magna aliqua. Sollicitudin ac orci phasellus egestas tellus rutrum tellus. Euismod elementum nisi quis eleifend quam adipiscing vitae proin sagittis. Egestas sed tempus urna et pharetra pharetra. Quis blandit turpis cursus in hac habitasse. Sed velit dignissim sodales ut eu. Ac auctor augue mauris augue neque. In arcu cursus euismod quis viverra nibh cras pulvinar mattis. Libero justo laoreet sit amet. Felis eget nunc lobortis mattis aliquam faucibus purus in. Pulvinar etiam non quam lacus suspendisse faucibus. Odio tempor orci dapibus ultrices. Velit dignissim sodales ut eu sem integer vitae justo. Fermentum et sollicitudin ac orci phasellus egestas. Pharetra vel turpis nunc eget lorem dolor sed. Sed turpis tincidunt id aliquet risus feugiat in ante. Mus mauris vitae ultricies leo integer malesuada nunc vel. Rhoncus urna neque viverra justo nec ultrices dui. Ut placerat orci nulla pellentesque dignissim enim sit amet.</p>
    <p>Bibendum arcu vitae elementum curabitur vitae nunc. Nunc pulvinar sapien et ligula ullamcorper malesuada. At elementum eu facilisis sed. Erat pellentesque adipiscing commodo elit at imperdiet dui accumsan sit. Nunc scelerisque viverra mauris in aliquam sem fringilla. In vitae turpis massa sed. Volutpat ac tincidunt vitae semper quis lectus nulla at. Massa placerat duis ultricies lacus sed turpis. Dui vivamus arcu felis bibendum ut tristique et egestas. Blandit aliquam etiam erat velit scelerisque in dictum non consectetur. Id neque aliquam vestibulum morbi blandit cursus risus at. Sed egestas egestas fringilla phasellus faucibus scelerisque eleifend donec. Ornare quam viverra orci sagittis eu volutpat odio facilisis. Volutpat sed cras ornare arcu dui vivamus arcu. Interdum consectetur libero id faucibus nisl.</p>
    <p>Viverra mauris in aliquam sem. Mattis molestie a iaculis at erat pellentesque adipiscing commodo elit. Sit amet volutpat consequat mauris nunc. Aliquam nulla facilisi cras fermentum. Sed turpis tincidunt id aliquet risus feugiat. Augue neque gravida in fermentum et sollicitudin ac orci.</p>
  </div>
  <div class="sign-area" role="img" aria-label="Handwritten signature of Daniel Reeve"></div>
  <div class="signer"><b>Daniel Reeve</b><i>Chief Director</i></div>
  <div class="band"><span>22-180 Birchwood Ave, Guelph, ON N1H 4K7</span></div>
</section>

<!-- compliments slip -->
<section class="piece compliments">
  <div class="logo"><div class="logo-row"><span class="logo-name">Brenvik</span><span class="logo-mark"></span></div><div class="logo-tag">Tape and Packaging Specialists</div></div>
  <div class="address">
    22-180 Birchwood Ave<br>Guelph, ON N1H 4K7
    <ul class="contacts">
      <li><svg><use href="#i-phone"/></svg>548-555-0142</li>
      <li><svg><use href="#i-mail"/></svg>info@brenviksales.com</li>
      <li><svg><use href="#i-web"/></svg>www.brenviksales.com</li>
    </ul>
  </div>
  <div class="band"><span>WITH COMPLIMENTS</span></div>
</section>

<!-- envelope, back -->
<section class="piece envelope-back">
  <svg class="flap" viewBox="0 0 294 48" aria-hidden="true"><path d="M0 0H294L289 30Q286 47 270 47H24Q8 47 5 30Z" fill="#231f20"/></svg>
  <div class="logo light"><div class="logo-row"><span class="logo-name">Brenvik</span><span class="logo-mark"></span></div><div class="logo-tag">Tape and Packaging Specialists</div></div>
</section>

<!-- envelope, front -->
<section class="piece envelope-front">
  <div class="logo"><div class="logo-row"><span class="logo-name">Brenvik</span><span class="logo-mark"></span></div><div class="logo-tag">Tape and Packaging Specialists</div></div>
  <div class="window"></div>
  <div class="band"><span>22-180 Birchwood Ave, Guelph, ON N1H 4K7</span></div>
</section>

<!-- folder, outside front -->
<section class="piece dark folder-cover">
  <div class="logo light"><div class="logo-row"><span class="logo-name">Brenvik</span><span class="logo-mark"></span></div><div class="logo-tag">Tape and Packaging Specialists</div></div>
  <div class="cover-lines">
    22-180 Birchwood Ave, Guelph, ON N1H 4K7
    <div class="rule"></div>
    548-555-0142 &nbsp;·&nbsp; info@brenviksales.com &nbsp;·&nbsp; www.brenviksales.com
  </div>
</section>

<!-- folder, outside back -->
<section class="piece folder-back">
  <div class="logo"><div class="logo-row"><span class="logo-name">Brenvik</span><span class="logo-mark"></span></div><div class="logo-tag">Tape and Packaging Specialists</div></div>
  <div class="band"><span>www.brenviksales.com</span></div>
</section>

<!-- folder, inside -->
<section class="piece folder-open">
  <div class="panel left">
    <svg class="pocket" viewBox="0 0 223 80" aria-hidden="true"><path d="M0 0H200Q206 0 208 6L223 80H0Z" fill="#231f20"/></svg>
    <div class="logo light"><div class="logo-row"><span class="logo-name">Brenvik</span><span class="logo-mark"></span></div><div class="logo-tag">Tape and Packaging Specialists</div></div>
  </div>
  <div class="panel right">
    <div class="mini-letter">
      <div class="logo"><div class="logo-row"><span class="logo-name">Brenvik</span><span class="logo-mark"></span></div><div class="logo-tag">Tape and Packaging Specialists</div></div>
      <ul class="contacts">
        <li><svg><use href="#i-phone"/></svg>548-555-0142</li>
        <li><svg><use href="#i-mail"/></svg>info@brenviksales.com</li>
        <li><svg><use href="#i-web"/></svg>www.brenviksales.com</li>
      </ul>
      <div class="recipient"><b>Dear. Mrs Clara Anne Whitfield</b><i>Chief Director</i></div>
      <div class="date">Date: 16-October-2025</div>
      <div class="letter-body"><p>Lorem ipsum dolor sit amet, consectetur adipiscing elit, sed do eiusmod tempor incididunt ut labore et dolore magna aliqua. Ut enim ad minim veniam, quis nostrud exercitation ullamco laboris nisi ut aliquip ex ea commodo consequat.</p></div>
      <div class="sign-area" role="img" aria-label="Handwritten signature of Daniel Reeve"></div>
      <div class="signer"><b>Daniel Reeve</b></div>
    </div>
    <svg class="pocket" viewBox="0 0 223 80" aria-hidden="true"><path d="M23 6Q25 0 31 0H223V80H0Z" fill="#231f20"/></svg>
    <div class="mini-card">
      <div class="logo"><div class="logo-row"><span class="logo-name">Brenvik</span><span class="logo-mark"></span></div><div class="logo-tag">Tape and Packaging Specialists</div></div>
      <div class="person">MARCUS DELANEY<i>Founder &amp; CEO</i></div>
      <ul class="contacts">
        <li>548-555-0142</li>
        <li>info@brenviksales.com</li>
        <li>www.brenviksales.com</li>
      </ul>
      <div class="band"><span>22-180 Birchwood Ave, Guelph, ON N1H 4K7</span></div>
    </div>
  </div>
</section>

</body>
</html>
```